Create a memorable Stationary for Security Software Company

TelVandrik is the worldwide leader in securing the Internet. Making Internet communications and critical data secure, reliable and available everywhere has been and continues to be our ongoing vision. We are committed to staying focused on real customer needs and to developing new and innovative security solutions that redefine the security landscape.

Industry/Entity Type

Internet

Font styles to use
Serif
Sans Serif
Script

Colors
0792cd
33a6d7
85cae6

```html
<!DOCTYPE html>
<html lang="en">
<head>
<meta charset="UTF-8">
<title>TelVandrik Business Card</title>
<link href="https://fonts.googleapis.com/css2?family=Source+Sans+3:wght@400;600;700&display=swap" rel="stylesheet">
<style>
  :root {
    --brand-blue: #0792cd;
    --brand-mid: #33a6d7;
    --brand-light: #85cae6;
    --paper: #ffffff;
    --ink: #4a4a4a;
    --stage: #e9ecef;
    --rule: #c9c9c9;
  }
  * { box-sizing: border-box; margin: 0; padding: 0; }
  html, body { width: 1200px; height: 1120px; overflow: hidden; }
  body {
    background: var(--stage);
    font-family: "Source Sans 3", "Myriad Pro", Arial, sans-serif;
    position: relative;
  }
  .card {
    position: absolute;
    width: 700px;
    height: 400px;
    overflow: hidden;
    box-shadow: 0 6px 18px rgba(0,0,0,0.18);
  }

  /* Front of card */
  .card-front {
    left: 160px; top: 70px;
    background: var(--brand-blue);
  }
  .front-mark {
    position: absolute;
    left: 0; right: 0; top: 56px;
    display: flex; flex-direction: column; align-items: center; gap: 8px;
  }
  .front-mark .mark-dot {
    width: 96px; height: 96px; border-radius: 50%;
    background: var(--brand-mid);
  }
  .front-mark .mark-name {
    font-size: 48px; font-weight: 700; color: var(--brand-mid); line-height: 1.1;
  }
  .front-url {
    position: absolute; left: 0; right: 0; bottom: 70px;
    text-align: center;
    color: var(--paper);
    font-size: 22px; letter-spacing: 4px;
  }

  /* Back of card */
  .card-back {
    left: 340px; top: 610px;
    background: var(--paper);
  }
  .back-band {
    position: absolute; left: 0; top: 0; width: 100%; height: 110px;
    background: var(--brand-blue);
  }
  .back-band-line {
    position: absolute; left: 0; top: 118px; width: 100%; height: 4px;
    background: var(--brand-blue);
  }
  .back-mark {
    position: absolute; left: 0; right: 0; top: 60px;
    display: flex; flex-direction: column; align-items: center; gap: 2px;
  }
  .back-mark .mark-dot {
    width: 92px; height: 92px; border-radius: 50%;
    background: var(--brand-light);
    border: 6px solid var(--paper);
  }
  .back-mark .mark-name {
    font-size: 36px; font-weight: 700; color: var(--brand-mid); line-height: 1.1;
  }
  .holder {
    position: absolute; right: 360px; top: 232px;
    text-align: right; color: var(--ink);
  }
  .holder-name { font-size: 26px; font-weight: 700; color: var(--brand-blue); line-height: 1.1; }
  .holder-title { font-size: 22px; margin-bottom: 18px; }
  .holder-address { font-size: 20px; line-height: 1.25; }
  .divider {
    position: absolute; left: 354px; top: 234px; width: 1px; height: 120px;
    background: var(--rule);
  }
  .contact-list {
    position: absolute; left: 370px; top: 230px;
    list-style: none; color: var(--ink); font-size: 20px;
  }
  .contact-list li { display: flex; align-items: center; gap: 10px; height: 30px; }
  .contact-list svg { width: 16px; height: 16px; fill: var(--brand-blue); flex: none; }
</style>
</head>
<body>

<section class="card card-front" aria-label="Card front">
  <div class="front-mark">
    <span class="mark-dot"></span>
    <span class="mark-name">TelVandrik</span>
  </div>
  <p class="front-url">www.telvandrik.com</p>
</section>

<section class="card card-back" aria-label="Card back">
  <div class="back-band"></div>
  <div class="back-band-line"></div>
  <div class="back-mark">
    <span class="mark-dot"></span>
    <span class="mark-name">TelVandrik</span>
  </div>

  <div class="holder">
    <p class="holder-name">Your Name</p>
    <p class="holder-title">Title</p>
    <p class="holder-address">Street Name, City Name<br>Zipcode-012345</p>
  </div>

  <div class="divider"></div>

  <ul class="contact-list">
    <li>
      <svg viewBox="0 0 16 16" aria-hidden="true"><path d="M3.5 1.5l2.5 0 1 3.5-1.8 1.2c.8 1.8 2.2 3.2 4 4l1.2-1.8 3.5 1v2.5c0 .8-.7 1.5-1.5 1.5C6.7 13.4 2.6 9.3 2 3c0-.8.7-1.5 1.5-1.5z"/></svg>
      012-345-6789
    </li>
    <li>
      <svg viewBox="0 0 16 16" aria-hidden="true"><path d="M4.5 0h7c.8 0 1.5.7 1.5 1.5v13c0 .8-.7 1.5-1.5 1.5h-7C3.7 16 3 15.3 3 14.5v-13C3 .7 3.7 0 4.5 0zM5 2v9h6V2zm3 10.5a1 1 0 100 2 1 1 0 000-2z"/></svg>
      012-345-6789
    </li>
    <li>
      <svg viewBox="0 0 16 16" aria-hidden="true"><path d="M1 3h14v10H1zM2 4.2v.4l6 4 6-4v-.4z"/></svg>
      info@telvandrik.com
    </li>
    <li>
      <svg viewBox="0 0 16 16" aria-hidden="true"><path d="M8 0a8 8 0 100 16A8 8 0 008 0zm5.9 7h-2.6c-.1-2-.6-3.8-1.4-5.1A6 6 0 0113.9 7zM8 2c.7 1 1.2 2.8 1.3 5H6.7C6.8 4.8 7.3 3 8 2zM6.1 1.9C5.3 3.2 4.8 5 4.700 7H2.1a6 6 0 014-5.1zM2.1 9h2.6c.1 2 .6 3.8 1.4 5.1A6 6 0 012.1 9zM8 14c-.7-1-1.2-2.8-1.3-5h2.6C9.2 11.2 8.7 13 8 14zm1.9.1c.8-1.3 1.3-3.1 1.4-5.1h2.6a6 6 0 01-4 5.1z"/></svg>
      www.telvandrik.com
    </li>
  </ul>
</section>

</body>
</html>
```